Web Design For Staffing Company

We need a homepage web design for a technical staffing company.

Please see attached brief for project details.

please make the site modern with bold colors while matching the logo

Be sure to read the attached breif in full beforehand.

Target Market(s)

technical companies looking to hire talent

Industry/Entity Type

Staffing

Number of Pages Required

1 page

Font styles to use
Sans Serif

```html
<!DOCTYPE html>
<html lang="en">
<head>
<meta charset="utf-8">
<title>Veltra Staffing — Technical Staffing</title>
<link href="https://fonts.googleapis.com/css2?family=Poppins:wght@300;400;500;600;700&family=Roboto:wght@300;400;500;700&display=swap" rel="stylesheet">
<style>
:root{
  --ink:#1c1c1c;
  --text:#5a5a5a;
  --muted:#8a8a8a;
  --brand:#2b5ea8;
  --nav-active:#3b8fd8;
  --navy-btn:#2c4a9a;
  --green:#2f9a18;
  --red:#e0180c;
  --blog:#2f87c7;
  --dark-band:#3a4358;
  --grey:#efefef;
  --footer:#0e2946;
  --footer-card:#173a60;
  --white:#ffffff;
}
*{box-sizing:border-box;margin:0;padding:0}
html,body{width:1200px;height:3628px;overflow:hidden}
body{position:relative;background:var(--white);font-family:'Roboto',sans-serif;color:var(--text)}
.abs{position:absolute}
.h{font-family:'Poppins',sans-serif}
.btn{position:absolute;display:flex;align-items:center;justify-content:center;color:var(--white);font-family:'Roboto',sans-serif;font-weight:500;font-size:21px;letter-spacing:.2px}
.btn-navy{background:var(--navy-btn)}
.btn-green{background:var(--green)}
.btn-red{background:var(--red)}

/* header & hero */
.hero-photo{left:0;top:0;width:1200px;height:669px;background:linear-gradient(180deg,#f4f4f4 0%,#d9dadd 30%,#3d4250 70%,#1d2029 100%)}
.brand{position:absolute;display:flex;align-items:center;gap:10px;font-family:'Poppins',sans-serif;font-weight:700;font-size:30px;color:var(--brand)}
.brand-dot{width:30px;height:30px;border-radius:50%;background:var(--brand)}
.nav{left:457px;top:28px;display:flex;gap:0;font-family:'Roboto',sans-serif;font-weight:500;font-size:13px;color:#2a2a2a}
.nav span{padding:7px 14px}
.nav .active{background:var(--nav-active);color:var(--white)}
.social{display:flex;gap:7px}
.social i{width:22px;height:22px;border-radius:50%;border:1.5px solid #444;display:block}
.search{left:251px;top:493px;display:flex;gap:10px}
.search div{height:42px;background:rgba(255,255,255,.88);font-size:13px;color:#777;display:flex;align-items:center;padding-left:20px}
.search .go{background:var(--navy-btn);color:var(--white);font-weight:500;justify-content:center;padding:0}
.promo{top:584px;height:159px;width:450px;display:flex;align-items:flex-start;justify-content:center;text-align:center;padding-top:43px;color:var(--white);font-family:'Poppins',sans-serif;font-weight:500;font-size:27px;line-height:33px}
.promo-left{left:151px;background:linear-gradient(135deg,#1f6fc2,#3a95dd 60%,#1b5aa6)}
.promo-right{left:600px;background:linear-gradient(135deg,#4a5466,#2f3848)}

/* about */
.about-photo{left:151px;top:852px;width:349px;height:255px;background:linear-gradient(180deg,#ffffff,#e8ebef 60%,#c9ced6)}
.section-title{font-family:'Poppins',sans-serif;font-size:27px;font-weight:300;color:var(--ink)}
.section-title b{font-weight:600}
.para{font-size:16px;line-height:22.5px}

/* dark band */
.dark-band{left:0;top:1107px;width:1200px;height:415px;background:var(--dark-band)}
.meeting-photo{left:151px;top:1198px;width:349px;height:234px;background:linear-gradient(135deg,#e9eef2,#b9c4cf 55%,#6f7d8c)}

/* grey */
.grey-band{left:0;top:1522px;width:1200px;height:321px;background:var(--grey)}

/* testimonial */
.center{left:0;width:1200px;text-align:center}

/* blog */
.blog-band{left:0;top:2225px;width:1200px;height:711px;background:var(--blog)}
.card{top:2330px;width:281px;height:531px;background:var(--white)}
.card-img{height:190px}
.card-body{padding:16px 16px 0}
.card-meta{font-size:12.5px;color:var(--muted);margin-bottom:4px}
.card-title{font-family:'Poppins',sans-serif;font-weight:600;font-size:14.5px;line-height:18px;color:var(--ink);margin-bottom:16px}
.card-text{font-size:12.5px;line-height:18px;color:#555}
.card-text p{margin-bottom:16px}
.more{font-size:12.5px;color:var(--blog);font-weight:500}

/* cta */
.cta{left:151px;top:2996px;width:898px;height:193px;background:linear-gradient(90deg,#5ee05a,#8ff07a 55%,#aef58f)}
.cta-person{left:151px;top:2996px;width:250px;height:193px;background:linear-gradient(180deg,#6bd865,#2c3a55)}
.cta-box{top:3016px;height:173px;background:rgba(255,255,255,.25);text-align:center;font-size:19px;line-height:24px;color:#222;padding-top:28px}

/* footer */
.footer{left:0;top:3253px;width:1200px;height:290px;background:var(--footer)}
.fcard{top:3292px;height:206px;background:var(--footer-card);padding:20px 19px;color:var(--white)}
.fcard h3{font-family:'Roboto',sans-serif;font-weight:500;font-size:22px;margin-bottom:20px}
.fcard p{font-size:13px;line-height:18px;margin-bottom:34px}
.fbtn{display:inline-flex;align-items:center;gap:10px;background:var(--navy-btn);height:34px;padding:0 22px 0 14px;font-size:16px;font-weight:500}
.bottom{left:0;top:3543px;width:1200px;height:85px;background:var(--white)}
</style>
</head>
<body>

<!-- header & hero -->
<div class="abs hero-photo" role="img" aria-label="Team of smiling business professionals in suits"></div>
<div class="brand" style="left:151px;top:20px"><span class="brand-dot"></span>Veltra</div>
<nav class="abs nav"><span class="active">HOME</span><span>ABOUT</span><span>JOB SEEKERS</span><span>CLIENTS</span><span>CONTACT</span></nav>
<div class="abs social" style="left:937px;top:31px"><i></i><i></i><i></i><i></i></div>

<div class="abs search">
  <div style="width:225px">Keyword</div>
  <div style="width:225px">Location</div>
  <div class="go" style="width:225px">SEARCH JOBS</div>
</div>

<div class="abs promo promo-left">The Right People<br>For The Right Jobs!</div>
<div class="abs promo promo-right">Bridging the talent gap<br>in Technical Staffing</div>
<div class="btn btn-green" style="left:284px;top:721px;width:182px;height:48px">HIRE TALENT</div>
<div class="btn btn-red" style="left:732px;top:721px;width:185px;height:48px">GET HIRED</div>

<!-- about -->
<div class="abs about-photo" role="img" aria-label="Group of professionals holding a company sign"></div>
<h2 class="abs section-title" style="left:549px;top:916px">Technical Staffing <b>Solutions Experts!</b></h2>
<p class="abs para" style="left:550px;top:967px;width:470px">Veltra Staffing is a National Technical Staffing and Recruiting Solutions Provider founded in 2013 focused on matching contract and full time Engineering and IT professionals with new and exciting employment opportunities!</p>

<!-- dark band -->
<div class="abs dark-band" role="img" aria-label="Dimmed photo of seated business people"></div>
<div class="abs meeting-photo" role="img" aria-label="Business team shaking hands at a meeting table"></div>
<h2 class="abs section-title" style="left:549px;top:1191px;color:var(--white)">Simply said... <b>WE LOVE TO RECRUIT!</b></h2>
<p class="abs para" style="left:550px;top:1245px;width:510px;color:#e8ebf0">It's our passion and we take it very seriously! It is not easy for JOB SEEKERS to put their job search efforts and trust in the hands of someone else,especially when there are so many Staffing Firms to choose from. So how do you know you are choosing the best Staffing Representation possible?</p>
<div class="btn btn-navy" style="left:550px;top:1384px;width:186px;height:48px">LEARN MORE</div>
<div class="btn btn-green" style="left:752px;top:1384px;width:184px;height:48px">VIEW JOBS</div>

<!-- grey -->
<div class="abs grey-band"></div>
<h2 class="abs h" style="left:151px;top:1583px;width:380px;font-size:28px;line-height:37px;color:#333;font-weight:400">Are you responsible for<br><b style="font-weight:600">Technical Staffing within your organization?</b></h2>
<p class="abs para" style="left:550px;top:1586px;width:500px;font-size:15.5px;line-height:24px">Are you satisfied with your current Supplier(s)' overall performance? Does it appear they identify potential Candidate(s) based purely on "buzz-word" searches? Is it evident they just do not grasp the scope and responsibilities of your technical staffing need(s)?</p>
<div class="btn btn-navy" style="left:550px;top:1738px;width:185px;height:48px">LEARN MORE</div>
<div class="btn btn-green" style="left:752px;top:1738px;width:184px;height:48px">HIRE TALENT</div>

<!-- testimonial -->
<div class="abs center" style="top:1895px;font-size:12.5px;font-weight:500;color:#333">TESTIMONIALS</div>
<h2 class="abs center h" style="top:1913px;font-size:27px;font-weight:600;color:var(--ink)">What our clients say about us.</h2>
<svg class="abs" style="left:582px;top:1973px" width="36" height="30" viewBox="0 0 36 30"><path d="M0 30V16C0 6 5 1 14 0v6c-5 1-7 4-7 9h7v15zM22 30V16c0-10 5-15 14-16v6c-5 1-7 4-7 9h7v15z" fill="#333"/></svg>
<p class="abs center" style="left:160px;width:880px;top:2034px;font-size:15.5px;line-height:24px;color:#6a6a6a">Marcus Hale is an excellent recruiter. He is articulate, honest, has a good nature and is an effective information conduit between his clients and candidates. He gave me the feeling he is there for the big picture desiring to forge a future relationship that will be mutually beneficial to both of us."</p>
<div class="abs center" style="top:2130px;font-size:11px;font-weight:700;color:#222"><span style="color:var(--blog)">SAM R.</span> – ELECTRICAL TEST ENGINEER IN THE AUTOMOTIVE SECTOR:</div>
<svg class="abs" style="left:580px;top:2160px" width="40" height="10"><circle cx="5" cy="5" r="3.5" fill="#2f87c7"/><circle cx="20" cy="5" r="3.5" fill="none" stroke="#2f87c7"/><circle cx="35" cy="5" r="3.5" fill="#2f87c7"/></svg>

<!-- blog -->
<div class="abs blog-band"></div>
<h2 class="abs center h" style="top:2266px;font-size:28px;font-weight:600;color:var(--white)">From our blog</h2>

<article class="abs card" style="left:151px">
  <div class="card-img" role="img" aria-label="Coworkers meeting around laptops" style="background:linear-gradient(135deg,#f4f6f8,#c8d0d8)"></div>
  <div class="card-body">
    <div class="card-meta">June 19, 2019 by veltrastaffing</div>
    <div class="card-title">Tips for Spotting a U.S. Recession Before It Becomes Official</div>
    <div class="card-text"><p>As the U.S. nears a record-long expansion in July, the conversation is increasingly turning to when it will all end.</p><p>Recessions are inherently hard to spot. The Lakeshore Institute of Market Studies' Economic Cycle Review Panel generally waits about a year to make a call.</p></div>
    <div class="more">▸ Read more</div>
  </div>
</article>
<article class="abs card" style="left:459px">
  <div class="card-img" role="img" aria-label="Woman working on a laptop" style="background:linear-gradient(135deg,#5a4a40,#1f2a3a)"></div>
  <div class="card-body">
    <div class="card-meta">June 17, 2019 by veltrastaffing</div>
    <div class="card-title">Ways To Make The Most Of The Hot Job Market</div>
    <div class="card-text"><p>"This is the tightest labor market I can remember. Unemployment is at a 50-year low and wage growth is at 3.2%," said Ned Porter, chief economist for JobBoard.com, during the fifth-annual JobBoard Interactive conference, held last month in Austin, Texas.</p><p>Over 1,800 recruiters and HR professionals attended the event, eager</p></div>
    <div class="more">▸ Read more</div>
  </div>
</article>
<article class="abs card" style="left:769px">
  <div class="card-img" role="img" aria-label="Business handshake over a desk" style="background:linear-gradient(135deg,#2d5a8c,#9bb4cc)"></div>
  <div class="card-body">
    <div class="card-meta">June 6, 2019 by veltrastaffing</div>
    <div class="card-title">Back To Basics: Meeting Employees' Needs To Improve Organizational Performance</div>
    <div class="card-text"><p>The benefits of employee satisfaction are well-established, so HR professionals and leaders across all industries spend a great deal of time focused on maximizing those benefits for organizational outcomes. There's no shortage of approaches in the pursuit of results, so when it comes to employee satisfaction, the focus should</p></div>
    <div class="more">▸ Read more</div>
  </div>
</article>

<!-- cta -->
<div class="abs cta"></div>
<div class="abs cta-person" role="img" aria-label="Smiling businesswoman pointing to the offers"></div>
<div class="abs cta-box" style="left:410px;width:305px">LOOKING FOR CAREER-MINDED<br>CANDIDATES?</div>
<div class="abs cta-box" style="left:736px;width:293px">LOOKING FOR CAREER<br>OPPORTUNITIES?</div>
<div class="btn btn-navy" style="left:451px;top:3098px;width:222px;height:47px">REQUEST TALENT</div>
<div class="btn btn-green" style="left:771px;top:3098px;width:227px;height:47px">SEARCH JOBS</div>

<!-- footer -->
<div class="abs footer"></div>
<div class="abs fcard" style="left:151px;width:290px">
  <h3>GET HIRED</h3>
  <p>Search our extensive list of available jobs to find your ideal match.</p>
  <span class="fbtn"><svg width="14" height="14" viewBox="0 0 14 14"><circle cx="5.5" cy="5.5" r="4" fill="none" stroke="#fff" stroke-width="2"/><path d="M8.5 8.5L13 13" stroke="#fff" stroke-width="2.2"/></svg>SEARCH NOW</span>
</div>
<div class="abs fcard" style="left:459px;width:291px">
  <h3>HIRE TALENT</h3>
  <p>Search our extensive list of available jobs to find your ideal match.</p>
  <span class="fbtn"><svg width="12" height="15" viewBox="0 0 12 15"><circle cx="6" cy="3" r="2.6" fill="#fff"/><path d="M2 15V8a4 4 0 018 0v7z" fill="#fff"/></svg>START TODAY</span>
</div>
<div class="abs fcard" style="left:772px;width:277px">
  <h3>GET IN TOUCH</h3>
  <p>Veltra Staffing, Inc.<br>220 Harbor Street, Suite 3<br>Lakeview, MA 01990</p>
  <span class="fbtn" style="margin-top:-16px"><svg width="16" height="12" viewBox="0 0 16 12"><rect width="16" height="12" fill="#fff"/><path d="M0 0l8 6 8-6" fill="none" stroke="#173a60" stroke-width="1.6"/></svg>CONTACT US</span>
</div>

<div class="abs bottom"></div>
<div class="brand" style="left:151px;top:3566px"><span class="brand-dot"></span>Veltra</div>
<div class="abs" style="left:318px;top:3578px;font-size:13px;color:#555">Copyright © 2020. All rights reserved.</div>
<div class="abs social" style="left:937px;top:3574px"><i></i><i></i><i></i><i></i></div>

</body>
</html>
```